Brellow Publishing

I made a website myself www.brellowpublishing.co.uk a few years ago but I need a new design, which I will code. One that I can be proud of, that 's sexy, to win new customers and showcase my publishing skills. This is a publishing website so I want the home page and books page to be fantastic. I have a logo already so will like the same colour scheme or thereabouts. I have current files and features that I would like to add to your creativity and experience.

Target Market(s)

Web Designers, Graphic Designers

Industry/Entity Type

Book Publisher

Number of Pages Required

5+ page

Font styles to use
Sans Serif

Colors
0255a3
ffffff
ec1f27

Requirements
Must have
• Menu and Sub Menu
• Footer
• Buy Page - Shopping Cart
• Upload feature on the submissions page
• video section on home page (how we publish books)
• Ad space section
Nice to have
• social media bar
• Zoom in page

```html
<!DOCTYPE html>
<html lang="en">
<head>
<meta charset="utf-8">
<title>Brellow Publishing</title>
<link href="https://fonts.googleapis.com/css2?family=Roboto:wght@300;400;500;700&display=swap" rel="stylesheet">
<style>
:root{
  --navy:#262b86;
  --blue:#2d3396;
  --orange:#f0521d;
  --white:#ffffff;
  --ink:#3a3a3a;
  --muted:#666a70;
  --grey-circle:#e4e4e4;
  --line:#d5d5d5;
  --footer:#2c2f36;
  --footer-deep:#23262c;
  --footer-text:#8a8e96;
}
*{margin:0;padding:0;box-sizing:border-box}
html,body{width:1200px;height:3327px;overflow:hidden;background:var(--white)}
body{font-family:"Roboto",Arial,sans-serif;color:var(--ink);position:relative}
.abs{position:absolute}
/* header */
.topbar{left:0;top:0;width:1200px;height:55px;background:var(--navy);z-index:3}
.logo-panel{left:168px;top:-20px;width:118px;height:150px;background:var(--white);transform:skewY(-28deg);transform-origin:top left;z-index:4;box-shadow:0 3px 8px rgba(0,0,0,.2)}
.logo-name{left:180px;top:62px;width:100px;text-align:center;font-size:14px;font-weight:500;color:var(--navy);z-index:5;line-height:1.15}
.nav{left:368px;top:27px;display:flex;gap:22px;z-index:5}
.nav a{font-size:11px;color:var(--white);text-decoration:none;font-weight:400;letter-spacing:.2px;padding-bottom:4px}
.nav a.active{color:var(--orange);border-bottom:2px solid var(--orange)}
.social{left:927px;top:24px;display:flex;gap:5px;z-index:5}
.social span{width:18px;height:18px;border-radius:50%;background:var(--white)}
/* hero */
.hero{left:0;top:0;width:1200px;height:588px;background:linear-gradient(110deg,#4a4e54 0%,#7b7670 30%,#b6a897 55%,#d9d4cf 80%,#eceae8 100%)}
.hero-title{left:168px;top:238px;font-size:28px;font-weight:700;color:var(--white);line-height:1.28}
.hero-text{left:168px;top:329px;font-size:12px;color:var(--white);line-height:1.4}
.btn{display:flex;align-items:center;justify-content:center;gap:14px;background:var(--orange);color:var(--white);font-size:11px;border-radius:20px;font-weight:500}
.hero-btn{left:169px;top:386px;width:133px;height:36px}
.arrow-box{top:306px;width:32px;height:32px;background:rgba(30,30,30,.75);display:flex;align-items:center;justify-content:center}
.dots{display:flex;gap:8px}
.dots span{width:11px;height:11px;border-radius:50%;background:var(--white)}
.dots span.on{background:var(--orange)}
/* band */
.band{left:0;top:588px;width:1200px;height:117px;background:var(--blue)}
.band-text{left:0;top:598px;width:1200px;text-align:center;font-size:23px;color:var(--white);font-weight:300}
.band-btn{left:532px;top:650px;width:134px;height:40px}
/* about */
.books-art{left:215px;top:765px;width:352px;height:388px;background:linear-gradient(135deg,#7a1b1b 0%,#b33a1d 35%,#d68f3a 60%,#3a5f8f 100%)}
.about-h{left:619px;top:804px;font-size:20px;font-weight:700;color:var(--orange);line-height:1.3}
.about-p{left:619px;top:873px;width:412px;font-size:12.4px;line-height:1.5;color:var(--muted)}
/* section headings */
.sec-h{left:0;width:1200px;text-align:center;font-size:26px;font-weight:300;color:var(--ink)}
.sec-h b{font-weight:300;color:var(--orange)}
.sec-h.light{color:var(--white)}
.divider{left:540px;width:120px;height:14px}
/* services */
.service{width:300px;text-align:center}
.svc-circle{width:156px;height:156px;border-radius:50%;background:var(--grey-circle);border:4px solid #f1f1f1;margin:0 auto;display:flex;align-items:center;justify-content:center}
.svc-title{margin-top:14px;font-size:16px;font-weight:500;color:#222}
.svc-text{margin:6px auto 0;width:190px;font-size:11.5px;line-height:1.45;color:var(--muted)}
/* video */
.video-sec{left:0;top:1568px;width:1200px;height:457px;background:linear-gradient(90deg,#2a2622 0%,#3b342c 40%,#4d4438 70%,#2e2a26 100%)}
.video-thumb{left:390px;top:1677px;width:422px;height:313px;background:radial-gradient(circle at 50% 45%,#f3ecd6 0%,#e6d7ae 55%,#c9b37d 100%);border:3px solid #c7a96b}
/* steps */
.step{width:220px;text-align:center}
.step-circle{width:92px;height:92px;border-radius:50%;border:3px solid #c9c9c9;background:var(--white);margin:0 auto;display:flex;align-items:center;justify-content:center;font-size:27px;font-weight:300;color:var(--orange)}
.step-title{margin-top:14px;font-size:12px;color:#333;letter-spacing:.3px}
.step-text{margin:8px auto 0;width:200px;font-size:10.5px;line-height:1.45;color:#444}
.step-line{top:2208px;left:262px;width:674px;border-top:1px dashed #bcbcbc}
/* partners */
.partners{left:160px;top:2511px;display:flex;gap:22px}
.partner{width:127px;height:84px;border:1px solid #d2d2d2;background:var(--white);display:flex;align-items:center;justify-content:center}
.partner i{display:block;width:78px;height:26px;border-radius:4px;background:#cfd2d8}
.p-arrow{top:2543px;width:20px;height:20px;background:var(--orange);display:flex;align-items:center;justify-content:center}
/* testimonial */
.client{left:0;top:2633px;width:1200px;height:443px;background:linear-gradient(180deg,#2f38a0 0%,#2a3296 60%,#252c86 100%)}
.avatar{left:539px;top:2740px;width:122px;height:122px;border-radius:50%;border:4px solid #4e7ed6;background:linear-gradient(160deg,#e9d3b8,#b98d6a)}
.quote{left:0;top:2853px;width:1200px;text-align:center;font-size:72px;color:#4b56b6;font-family:Georgia,serif;line-height:1}
.client-text{left:230px;top:2940px;width:740px;text-align:center;font-size:12.5px;line-height:1.45;color:var(--white)}
/* footer */
.footer{left:0;top:3076px;width:1200px;height:200px;background:var(--footer)}
.foot-h{font-size:10px;color:#b3b6bd;letter-spacing:.4px;padding-bottom:6px;border-bottom:1px solid #40444c;width:190px}
.foot-col{top:3112px;font-size:9.5px;line-height:1.6;color:var(--footer-text)}
.foot-col p{margin-top:10px}
.foot-social{display:flex;gap:8px;margin-top:10px}
.foot-social span{width:10px;height:10px;border-radius:50%;background:#6f737b}
.contact-row{display:flex;gap:8px;align-items:flex-start;margin-top:8px}
.links{display:grid;grid-template-columns:110px 80px;row-gap:8px;margin-top:12px}
.sub-input{margin-top:14px;width:200px;height:30px;border:1px solid #4a4e56;display:flex;justify-content:flex-end;align-items:center;padding-right:8px}
.footbar{left:0;top:3276px;width:1200px;height:51px;background:var(--footer-deep)}
.footbar-l{left:160px;top:3296px;font-size:8.5px;color:var(--footer-text)}
.footbar-r{left:900px;width:140px;text-align:right;top:3296px;font-size:8.5px;color:var(--footer-text)}
</style>
</head>
<body>

<!-- hero -->
<div class="abs hero" role="img" aria-label="Photo of a smiling woman with glasses holding a cup at a laptop"></div>
<div class="abs topbar"></div>
<div class="abs logo-panel"></div>
<div class="abs logo-name">Brellow<br>Publishing</div>
<nav class="abs nav">
  <a class="active">HOME</a><a>PUBLISHING</a><a>SUBMISSIONS</a><a>BOOKS</a><a>AUTHORS</a><a>SEMINARS</a><a>CONTACT</a>
</nav>
<div class="abs social"><span></span><span></span><span></span><span></span><span></span></div>

<h1 class="abs hero-title">BRELLOW PUBLISHING<br>SELF-PUBLISHING THAT WORKS</h1>
<p class="abs hero-text">WELCOME TO BRELLOW PUBLISHING, WE ARE A NEW INDEPENDENT<br>PUBLISHING COMPANY LOCATED IN LONDON/SURREY</p>
<div class="abs btn hero-btn">READ MORE
  <svg width="7" height="10" viewBox="0 0 7 10"><path d="M1 1l4 4-4 4" stroke="#fff" stroke-width="1.6" fill="none"/></svg></div>
<div class="abs arrow-box" style="left:27px"><svg width="8" height="12" viewBox="0 0 8 12"><path d="M6 1L1 6l5 5" stroke="#fff" stroke-width="1.8" fill="none"/></svg></div>
<div class="abs arrow-box" style="left:1140px"><svg width="8" height="12" viewBox="0 0 8 12"><path d="M2 1l5 5-5 5" stroke="#fff" stroke-width="1.8" fill="none"/></svg></div>
<div class="abs dots" style="left:580px;top:553px"><span></span><span class="on"></span></div>

<!-- submit band -->
<div class="abs band"></div>
<p class="abs band-text">Lorem ipsum dolor sit amet, consectetur adipiscing elit.</p>
<div class="abs btn band-btn">SUBMIT BOOK
  <svg width="7" height="10" viewBox="0 0 7 10"><path d="M1 1l4 4-4 4" stroke="#fff" stroke-width="1.6" fill="none"/></svg></div>

<!-- about -->
<div class="abs books-art" role="img" aria-label="Three published book covers standing together"></div>
<h2 class="abs about-h">HAVE A STORY TO TELL?<br>WE CAN HELP YOU PUBLISH YOUR BOOK.</h2>
<p class="abs about-p">Welcome to Brellow Publishing, we are an independent publishing company located in London/Surrey. We publish Trade (fiction and non-fiction), &amp; Young Adult (YA) in a variety of subjects Lorem ipsum dolor sit amet, consectetur adipiscing elit. Integer iaculis quam et accumsan imperdiet. Nunc porta malesuada nunc sed molestie. Duis ultrices consectetur dolor sit amet semper. Aliquam erat volutpat. Sed massa tortor, lobortis fermentum elementum nec, iaculis sit amet justo. Suspendisse augue eros, volutpat a ultricies at, dignissim a mi. Curabitur nec nibh eu justo ultrices vestibulum. Sed libero turpis, tristique quis purus quis, condimentum elementum turpis. Fusce tristique neque sem, ultricies lacinia odio pellentesque sit amet. Ut aliquam eu nisl quis tempus.</p>

<!-- what we do -->
<h2 class="abs sec-h" style="top:1191px"><b>WHAT</b> WE DO</h2>
<svg class="abs divider" style="top:1227px" viewBox="0 0 120 14"><line x1="0" y1="7" x2="48" y2="7" stroke="#cfcfcf"/><line x1="72" y1="7" x2="120" y2="7" stroke="#cfcfcf"/><path d="M52 7l15-5-5 10-3-4z" fill="#9a9a9a"/></svg>

<div class="abs service" style="left:152px;top:1278px">
  <div class="svc-circle"><svg width="70" height="60" viewBox="0 0 70 60"><path d="M35 10C26 4 14 3 4 5v46c10-2 22-1 31 5z" fill="#f0521d"/><path d="M35 10c9-6 21-7 31-5v46c-10-2-22-1-31 5z" fill="#f0521d"/><line x1="35" y1="10" x2="35" y2="56" stroke="#e4e4e4" stroke-width="3"/></svg></div>
  <h3 class="svc-title">BOOKS</h3>
  <p class="svc-text">Lorem ipsum dolor sit amet, consectetur adipiscing elit. Integer iaculis quam et accumsan imperdiet.</p>
</div>
<div class="abs service" style="left:449px;top:1278px">
  <div class="svc-circle"><svg width="70" height="72" viewBox="0 0 70 72"><circle cx="28" cy="20" r="15" fill="#f0521d"/><path d="M2 70c0-18 12-30 26-30s26 12 26 30z" fill="#f0521d"/><path d="M46 62l16-24 6 4-16 24-8 3z" fill="#f0521d" stroke="#e4e4e4" stroke-width="2"/></svg></div>
  <h3 class="svc-title">AUTHORS</h3>
  <p class="svc-text">Lorem ipsum dolor sit amet, consectetur adipiscing elit. Integer iaculis quam et accumsan imperdiet.</p>
</div>
<div class="abs service" style="left:748px;top:1278px">
  <div class="svc-circle"><svg width="62" height="70" viewBox="0 0 62 70"><rect x="2" y="8" width="58" height="60" rx="9" fill="#f0521d"/><rect x="20" y="2" width="22" height="12" rx="4" fill="#f0521d" stroke="#e4e4e4" stroke-width="2"/><rect x="14" y="28" width="34" height="5" rx="2" fill="#fff"/><rect x="14" y="40" width="26" height="5" rx="2" fill="#fff"/><rect x="14" y="52" width="18" height="5" rx="2" fill="#fff"/></svg></div>
  <h3 class="svc-title">SUBMISSIONS</h3>
  <p class="svc-text">Lorem ipsum dolor sit amet, consectetur adipiscing elit. Integer iaculis quam et accumsan imperdiet.</p>
</div>

<!-- video -->
<div class="abs video-sec" role="img" aria-label="Dimmed photo of a reader in a library"></div>
<h2 class="abs sec-h light" style="top:1596px"><b>LEARN HOW</b> WE PUBLISH BOOKS</h2>
<svg class="abs divider" style="top:1633px" viewBox="0 0 120 14"><line x1="0" y1="7" x2="48" y2="7" stroke="#bbb"/><line x1="72" y1="7" x2="120" y2="7" stroke="#bbb"/><path d="M52 7l15-5-5 10-3-4z" fill="#ddd"/></svg>
<div class="abs video-thumb" role="img" aria-label="Video preview of manuscript papers and stationery on a desk"></div>
<svg class="abs" style="left:592px;top:1821px" width="18" height="24" viewBox="0 0 18 24"><path d="M0 0l18 12L0 24z" fill="#e3262a"/></svg>

<!-- steps -->
<h2 class="abs sec-h" style="top:2068px"><b>PUBLISH YOUR BOOK</b> IN 4 EASY STEPS</h2>
<svg class="abs divider" style="top:2104px" viewBox="0 0 120 14"><line x1="0" y1="7" x2="48" y2="7" stroke="#cfcfcf"/><line x1="72" y1="7" x2="120" y2="7" stroke="#cfcfcf"/><path d="M52 7l15-5-5 10-3-4z" fill="#9a9a9a"/></svg>
<div class="abs step-line"></div>
<div class="abs step" style="left:152px;top:2162px"><div class="step-circle">01</div><h3 class="step-title">WRITING</h3><p class="step-text">You write a book to the best of your ability and after redrafting several times when you honestly feel that you have done the best you possibly can with it, you send it to us</p></div>
<div class="abs step" style="left:376px;top:2162px"><div class="step-circle">02</div><h3 class="step-title">SUBMISSION</h3><p class="step-text">If your book is in our subject matter and you think you have something that could tickle our fancy, send us your book for review.</p></div>
<div class="abs step" style="left:602px;top:2162px"><div class="step-circle">03</div><h3 class="step-title">REVIEW</h3><p class="step-text">You send us your book and our editorial team will look over it and decide if we like it and</p></div>
<div class="abs step" style="left:826px;top:2162px"><div class="step-circle">04</div><h3 class="step-title">CONTRACT</h3><p class="step-text">You send us your book and our editorial team will look over it and decide if we like it and then we will decide what</p></div>

<!-- partners -->
<h2 class="abs sec-h" style="top:2424px"><b>WE</b> WORK WITH</h2>
<svg class="abs divider" style="top:2460px" viewBox="0 0 120 14"><line x1="0" y1="7" x2="48" y2="7" stroke="#cfcfcf"/><line x1="72" y1="7" x2="120" y2="7" stroke="#cfcfcf"/><path d="M52 7l15-5-5 10-3-4z" fill="#9a9a9a"/></svg>
<div class="abs partners">
  <div class="partner"><i></i></div><div class="partner"><i></i></div><div class="partner"><i></i></div>
  <div class="partner"><i></i></div><div class="partner"><i></i></div><div class="partner"><i></i></div>
</div>
<div class="abs p-arrow" style="left:163px"><svg width="6" height="9" viewBox="0 0 6 9"><path d="M5 1L1 4.5 5 8" stroke="#fff" stroke-width="1.5" fill="none"/></svg></div>
<div class="abs p-arrow" style="left:1017px"><svg width="6" height="9" viewBox="0 0 6 9"><path d="M1 1l4 3.5L1 8" stroke="#fff" stroke-width="1.5" fill="none"/></svg></div>

<!-- testimonial -->
<div class="abs client" role="img" aria-label="Blue-tinted collage of client portraits"></div>
<h2 class="abs sec-h light" style="top:2666px"><b>CLIENT</b> SPEAK</h2>
<svg class="abs divider" style="top:2702px" viewBox="0 0 120 14"><line x1="0" y1="7" x2="48" y2="7" stroke="#8a90d0"/><line x1="72" y1="7" x2="120" y2="7" stroke="#8a90d0"/><path d="M52 7l15-5-5 10-3-4z" fill="#d0d3f0"/></svg>
<div class="abs avatar" role="img" aria-label="Client portrait"></div>
<div class="abs quote">&ldquo;</div>
<p class="abs client-text">Lorem ipsum dolor sit amet, consectetur adipiscing elit. Integer iaculis quam et accumsan imperdiet. Nunc porta malesuada nunc sed molestie. Duis ultrices consectetur dolor sit amet semper. Aliquam erat volutpat. Sed massa tortor, lobortis fermentum elementum nec, iaculis sit amet justo.</p>
<div class="abs dots" style="left:583px;top:3035px"><span class="on"></span><span></span><span></span></div>

<!-- footer -->
<div class="abs footer"></div>
<div class="abs foot-col" style="left:160px">
  <h4 class="foot-h">COMPANY OVERVIEW</h4>
  <p style="width:190px">LOREM IPSUM DOLOR SIT AMET, CONSECTETUR ADIPISCING ELIT. MORBI TORTOR ANTE, TINCIDUNT QUIS DICTUM VEL, CONSECTETUR IN ODIO.</p>
  <div class="foot-social"><span></span><span></span><span></span><span></span><span></span></div>
</div>
<div class="abs foot-col" style="left:384px">
  <h4 class="foot-h">GET IN TOUCH</h4>
  <div class="contact-row" style="margin-top:12px"><svg width="8" height="11" viewBox="0 0 8 11"><path d="M4 11S0 6 0 4a4 4 0 018 0c0 2-4 7-4 7z" fill="#8a8e96"/></svg><span>Brellow Publishing Ltd 42 Harwick Lane<br>London</span></div>
  <div class="contact-row"><svg width="10" height="8" viewBox="0 0 10 8"><rect width="10" height="8" fill="#8a8e96"/><path d="M0 0l5 4 5-4" stroke="#2c2f36" fill="none"/></svg><span>info@brellowpublishing.co.uk</span></div>
  <div class="contact-row"><svg width="8" height="10" viewBox="0 0 8 10"><rect x="1" width="6" height="10" rx="1" fill="#8a8e96"/></svg><span>07400 123456</span></div>
</div>
<div class="abs foot-col" style="left:610px">
  <h4 class="foot-h">QUICK LINKS</h4>
  <div class="links"><span>Submissions</span><span>Seminars</span><span>Books</span><span>Contact</span><span>Authors</span><span>Ebooks</span><span>Production</span><span>Packages</span></div>
</div>
<div class="abs foot-col" style="left:836px">
  <h4 class="foot-h">SUBSCRIBE</h4>
  <div class="sub-input"><svg width="8" height="8" viewBox="0 0 8 8"><path d="M1 4h6M4 1l3 3-3 3" stroke="#8a8e96" fill="none"/></svg></div>
  <p style="width:200px">maximus tempor tincidunt et labore et dolore magna aliqua.</p>
</div>
<div class="abs footbar"></div>
<div class="abs footbar-l">COPYRIGHT © 2016 BRELLOWPUBLISHING</div>
<div class="abs footbar-r">FAQ &nbsp;|&nbsp; TERMS OF USE &nbsp;|&nbsp; PRIVACY POLICY</div>

</body>
</html>
```